Marwick Estate Services (Handyman / Home Improvement Company)

Looking for a double sided professional looking business card with Logo attached to be highlighted on one side and throwing in an image of a handyman as an option would be nice to see as well. We are a company focused on providing quality Handyman and Home improvement services in a timely manner that is done right the first time with integrity

Industry/Entity Type

Handyman / Home Improvement

Contact Information for Business Card

(LOGO, Name, Mobile and office phone numbers, email) on front side of card, (the words "The SOLUTION to all of your Handyman and Home Improvement needs" followed by "Family Owned and Operated" at the very bottom) on the back.

Colors
EB3D1F
EC4F4E
F09395
F8D3D4
FCEDEE

Requirements
Must have
• Red, Gray, Black Color scheme
Should not have
• No Yellow or Blue colors

```html
<!DOCTYPE html>
<html lang="en">
<head>
<meta charset="utf-8">
<title>Marwick Estate Services – Business Card</title>
<link rel="stylesheet" href="https://fonts.googleapis.com/css2?family=Lato:ital,wght@0,400;0,700;0,900;1,400&display=swap">
<style>
  :root{
    --stage:#3b3e41;
    --card-black:#1d1d1f;
    --brand-red:#e8141f;
    --ink:#141414;
    --paper:#ffffff;
    --steel:#8c8f93;
  }
  *{box-sizing:border-box;margin:0;padding:0}
  html,body{width:1200px;height:1122px;overflow:hidden}
  body{background:var(--stage);font-family:"Lato",sans-serif;position:relative}
  .card{position:absolute;left:170px;width:860px;height:491px;border-radius:34px;overflow:hidden}
  .card--back{top:50px;background:var(--card-black);color:var(--paper)}
  .card--front{top:581px;background:var(--paper)}

  /* back side */
  .back__brand{position:absolute;top:120px;left:0;right:0;display:flex;align-items:center;justify-content:center;gap:18px}
  .brand-dot{width:34px;height:34px;border-radius:50%;background:var(--brand-red)}
  .back__brand .brand-name{font-weight:900;font-size:44px;letter-spacing:1px;text-transform:uppercase;color:var(--paper)}
  .back__tagline{position:absolute;top:278px;left:0;right:0;text-align:center;font-weight:900;font-size:27px;line-height:1.3;letter-spacing:.5px;text-transform:uppercase}
  .back__tagline .accent{color:var(--brand-red)}
  .back__note{position:absolute;top:372px;left:0;right:0;text-align:center;color:var(--brand-red);font-style:italic;font-size:22px}

  /* front side */
  .front__panel{position:absolute;inset:0;width:860px;height:491px}
  .front__brand{position:absolute;left:50px;top:190px;width:250px;display:flex;align-items:center;gap:14px}
  .front__brand .brand-dot{background:var(--ink);flex:none}
  .front__brand .brand-name{font-weight:900;font-size:27px;line-height:1.1;text-transform:uppercase;color:var(--ink)}
  .contact{position:absolute;left:520px;right:50px;top:92px;color:var(--paper);white-space:nowrap}
  .contact__name{font-weight:900;font-size:34px;letter-spacing:1px;text-transform:uppercase;line-height:1.15}
  .contact__role{font-size:22px;margin-top:4px;margin-bottom:26px}
  .contact__list{list-style:none}
  .contact__item{display:flex;align-items:center;gap:14px;font-size:20px;line-height:1.8}
  .contact__icon{width:20px;height:20px;flex:none}
</style>
</head>
<body>

<section class="card card--back" aria-label="Business card back">
  <div class="back__brand">
    <span class="brand-dot"></span>
    <span class="brand-name">Marwick Estate Services</span>
  </div>
  <p class="back__tagline">Your <span class="accent">Solution</span> to all of your<br>Handyman &amp; Home Improvement Needs</p>
  <p class="back__note">Family Owned &amp; Operated</p>
</section>

<section class="card card--front" aria-label="Business card front">
  <svg class="front__panel" viewBox="0 0 860 491" aria-hidden="true">
    <rect x="500" y="0" width="360" height="491" fill="var(--brand-red)"/>
    <circle cx="530" cy="265" r="225" fill="var(--brand-red)"/>
  </svg>

  <div class="front__brand">
    <span class="brand-dot"></span>
    <span class="brand-name">Marwick Estate Services</span>
  </div>

  <div class="contact">
    <h1 class="contact__name">Daniel Carver</h1>
    <p class="contact__role">Founder &amp; CEO</p>
    <ul class="contact__list">
      <li class="contact__item">
        <svg class="contact__icon" viewBox="0 0 24 24"><path fill="#fff" d="M6.6 10.8a15 15 0 0 0 6.6 6.6l2.2-2.2a1 1 0 0 1 1-.25 11.4 11.4 0 0 0 3.6.6 1 1 0 0 1 1 1V20a1 1 0 0 1-1 1A17 17 0 0 1 3 4a1 1 0 0 1 1-1h3.5a1 1 0 0 1 1 1c0 1.25.2 2.45.6 3.6a1 1 0 0 1-.25 1z"/></svg>
        (123) 456-7890
      </li>
      <li class="contact__item">
        <svg class="contact__icon" viewBox="0 0 24 24"><rect x="6" y="2" width="12" height="20" rx="2" fill="none" stroke="#fff" stroke-width="2"/><circle cx="12" cy="18" r="1.2" fill="#fff"/></svg>
        (123) 456-7890
      </li>
      <li class="contact__item">
        <svg class="contact__icon" viewBox="0 0 24 24"><rect x="2" y="5" width="20" height="14" rx="1.5" fill="#fff"/><path d="M3 6l9 7 9-7" fill="none" stroke="var(--brand-red)" stroke-width="1.6"/></svg>
        info@marwickestate.com
      </li>
      <li class="contact__item">
        <svg class="contact__icon" viewBox="0 0 24 24"><circle cx="12" cy="12" r="9.5" fill="none" stroke="#fff" stroke-width="2"/><path d="M2.5 12h19M12 2.5c3 3 3 16 0 19M12 2.5c-3 3-3 16 0 19" fill="none" stroke="#fff" stroke-width="1.6"/></svg>
        marwickestate.com
      </li>
    </ul>
  </div>
</section>

</body>
</html>
```